New Corporate Business Card - Velmorabelle

What we need:
We need a new corporate business card.
We want a new template that we can change by ourself.
We want business card modern and minimalist but that looks professional.
We will print it in 300 gr soft-touch.
Why not a white side with the logo and a red/grey side with the content?
Why not a grey side and a red side like our logo?
I am sure that you have better idea than ours that's the reason we come here.

Who we are:
We are a private label company in cosmetics based in Switzerland. We work in BtoB. We make skin care products for other brands.

Target Market(s)

B to B - Worldwide - any gender

Industry/Entity Type

Cosmetics

Contact Information for Business Card

Side 1:
Logo
Your Swiss Private Label Manufacturer or www.velmorabelle.ch

Side 2:
Name and surname (Example: Lucien Marchetaz)
Job Description (General Manager)
Telephone (+41 32 918 64 00)
Direct (+41 32 918 64 64)
Email (lucien.marchetaz@velmorabelle.ch)
Chemin des Prés-Fleuris 14, 2000 Neuchâtel, Switzerland
www.velmorabelle.ch

Font styles to use
Serif
Sans Serif

Requirements
Must have
• You can use 4 colors: white, red, grey and/or black .
Should not have
• Too much colors, too much things. We want it simple!

```html
<!DOCTYPE html>
<html lang="en">
<head>
<meta charset="utf-8">
<title>Velmorabelle – Business Card</title>
<link href="https://fonts.googleapis.com/css2?family=Jost:wght@400;600&display=swap" rel="stylesheet">
<style>
  :root {
    --red: #ee3040;
    --grey: #a7a9ac;
    --grey-line: #b3b5b8;
    --white: #ffffff;
    --ink: #222222;
    --ink-soft: #555555;
    --backdrop: #e6e6e6;
  }
  * { margin: 0; padding: 0; box-sizing: border-box; }
  html, body { width: 1200px; height: 1000px; overflow: hidden; }
  body {
    position: relative;
    background: var(--backdrop);
    font-family: "Jost", "Helvetica Neue", Arial, sans-serif;
  }
  .card {
    position: absolute;
    left: 346px;
    width: 516px;
    height: 295px;
    overflow: hidden;
  }
  /* Front side */
  .card-front { top: 195px; background: var(--red); }
  .card-front .grey-half {
    position: absolute; left: 0; top: 0; width: 100%; height: 145px;
    background: var(--grey);
  }
  .brand {
    position: absolute; left: 0; top: 118px; width: 100%;
    display: flex; justify-content: center; align-items: center; gap: 12px;
    color: var(--white);
  }
  .brand-square { width: 22px; height: 22px; background: var(--white); }
  .brand-name {
    font-size: 40px; font-weight: 400; letter-spacing: 5px; line-height: 1;
  }
  .tagline {
    position: absolute; left: 0; top: 241px; width: 100%;
    text-align: center; color: var(--white);
    font-size: 16px; font-weight: 400;
  }
  /* Back side */
  .card-back { top: 521px; background: var(--white); }
  .card-frame { position: absolute; left: 0; top: 0; }
  .name-band {
    position: absolute; left: 0; top: 73px; width: 256px; height: 72px;
    background: var(--red); color: var(--white);
    text-align: right; padding: 13px 14px 0 0;
  }
  .person-name { font-size: 21px; font-weight: 400; line-height: 24px; }
  .person-name strong { font-weight: 600; }
  .person-role { font-size: 20px; line-height: 24px; }
  .address {
    position: absolute; left: 270px; top: 93px;
    color: var(--ink-soft); font-size: 16px; line-height: 20px;
  }
  .phones {
    position: absolute; left: 36px; top: 169px;
    color: var(--ink); font-size: 16px; line-height: 20px;
  }
  .phone-line { display: flex; align-items: center; gap: 8px; }
  .phone-line svg { width: 14px; height: 14px; fill: var(--red); }
  .web-band {
    position: absolute; left: 215px; top: 152px; width: 301px; height: 72px;
    background: var(--grey); color: var(--white);
    padding: 16px 0 0 15px; font-size: 16px; line-height: 20px;
  }
</style>
</head>
<body>

  <section class="card card-front" aria-label="Business card front">
    <div class="grey-half"></div>
    <div class="brand">
      <span class="brand-square"></span>
      <span class="brand-name">Velmorabelle</span>
    </div>
    <p class="tagline">Your Swiss Private Label Manufacturer</p>
  </section>

  <section class="card card-back" aria-label="Business card back">
    <svg class="card-frame" width="516" height="295" viewBox="0 0 516 295" aria-hidden="true">
      <rect x="18" y="22" width="476" height="253" fill="none" stroke="var(--grey-line)" stroke-width="4"/>
    </svg>

    <div class="name-band">
      <p class="person-name">LUCIEN <strong>MARCHETAZ</strong></p>
      <p class="person-role">General Manager</p>
    </div>

    <p class="address">Chemin des Prés-Fleuris 14<br>2000 Neuchâtel, Switzerland</p>

    <div class="phones">
      <p class="phone-line">
        <svg viewBox="0 0 14 14" aria-label="Telephone"><path d="M4 0h6a1.5 1.5 0 0 1 1.5 1.5v11A1.5 1.5 0 0 1 10 14H4a1.5 1.5 0 0 1-1.5-1.5v-11A1.5 1.5 0 0 1 4 0zm0.5 1.8v9.4h5V1.8z"/></svg>
        +41 32 918 64 00
      </p>
      <p class="phone-line">
        <svg viewBox="0 0 14 14" aria-label="Direct line"><path d="M1 5c0-2 3-3.5 6-3.5S13 3 13 5v1.2H10V4.8H4v1.4H1zM3 7h8l2 6H1z"/></svg>
        +41 32 918 64 64
      </p>
    </div>

    <div class="web-band">
      <p>lucien.marchetaz@velmorabelle.ch</p>
      <p>www.velmorabelle.ch</p>
    </div>
  </section>

</body>
</html>
```